Cover for nonfiction/memoir book "Static Beneath My Skin"

We're looking for a *nonfiction* *memoir* look that is consistent with other covers in that genre.

MUST HAVE:
- It must include the BACK COVER as it will be for print as well as an ebook.
- Title: Static Beneath My Skin
- TITLE MUST BE EASILY READ AT BRINDLECART THUMBNAIL SIZE
- Author name: Dorothea Quell
- At least one of the attached photos of Dorothea
- In COLOR
- The synopsis below
- Space for an endorsement

From the author: "I am looking for a cover that is eye catching and interesting or artistic, rather than just glamorous or pretty. If you like to edit the photos please do not completely remove the wrinkle between my eyebrows as I mention this in the book. It is okay if i look non conventional and my inner Aspie shows a little. The book is a little bit girly, and it would be good for the cover to reflect that, but mildly. No bright pink and purple designs. Please feel free to zoom in or crop the photos as you think works best"

SYNOPSIS (needs to go on the back cover)

Static Beneath My Skin is an acutely honest and often highly entertaining memoir by Dorothea Quell about life with Asperger's Syndrome. The book follows Dorothea in exploring her past and takes the reader with her on her journey to receiving and accepting her diagnosis. Instead of rehashing widely available Asperger's information, Dorothea focuses on discussing the thoughts, feelings and ideas that go along with being an Aspie, giving us a rare peek into what it really feels like to be a person on the spectrum. A must read for all those who enjoy deep personal stories or have a loved one on the spectrum that they wish to understand better.

The book dimensions will be 5x8 trade paperback and 6x9 hardcover (plus 0.25 bleed margin on all sizes - for both sizes).
Here is some more information from the publisher on cover requirements:

"I've attached a sample of both a paperback and hardcover size. Note that the spine width will be different depending on the final length of the book, so it won't be exact. That said, the front and back covers, and the flaps (for the hardcover) will always be the same as shown.
For deliverables, we need the following:

a Creative Suite 6 or earlier native .PSD (Photoshop), .ID (InDesign), or .AI (Illustrator) file. Creative Cloud files cannot be used and will not be accepted.
final file must include layered objects, and cannot be one 'background' image
Final files must be in CMYK color mode, 300dpi minimum
Total Ink saturation must be no more than 240% on any part of the cover. "True" black should use the following CMYK values: 60/40/40/100.
Fonts used in creation of the cover must be either A) embedded or B) sent with the final file
Vector art is preferred for scaling purposes"

Target Market(s)

Women of all ages. People who like psychology and personal stories.
Also parents and family members who may have a loved one on the Autism spectrum.

Requirements
Nice to have
• Bright green new leaves and greenery are good but not necessary.

```html
<!DOCTYPE html>
<html lang="en">
<head>
<meta charset="utf-8">
<title>Static Beneath My Skin — Cover Spread</title>
<link href="https://fonts.googleapis.com/css2?family=Cinzel:wght@400;500&family=Montserrat:wght@400;500;600&display=swap" rel="stylesheet">
<style>
  :root {
    --ink-white: #ffffff;
    --spine-green: #4c7a3c;
    --back-deep: #3e5a3a;
    --back-mid: #7d8d5c;
    --back-light: #a9ab7a;
    --land-teal: #6f8f86;
    --land-green: #5f7a4a;
    --hair-gold: #c9a46e;
    --hair-copper: #a8703f;
    --skin-light: #f0c9a0;
    --skin-warm: #d99a6c;
    --top-navy: #1f2a3e;
    --top-red: #b8452f;
    --shadow: rgba(0, 0, 0, 0.55);
  }
  * { margin: 0; padding: 0; box-sizing: border-box; }
  html, body { width: 1200px; height: 864px; overflow: hidden; background: #222; }
  .cover-spread { position: relative; width: 1200px; height: 864px; overflow: hidden; }

  .back-cover { position: absolute; left: 0; top: 0; width: 576px; height: 864px; }
  .back-backdrop {
    position: absolute; inset: 0;
    background:
      radial-gradient(ellipse 45% 30% at 15% 20%, #4e5e3c 0%, transparent 100%),
      radial-gradient(ellipse 60% 20% at 50% 58%, #c2b888 0%, transparent 100%),
      radial-gradient(ellipse 70% 25% at 40% 85%, #5b7040 0%, transparent 100%),
      linear-gradient(180deg, var(--back-deep) 0%, #6c8050 35%, var(--back-light) 60%, #8f9a66 75%, #4f663a 100%);
  }
  .spine { position: absolute; left: 576px; top: 0; width: 48px; height: 864px; background: var(--spine-green); }
  .front-cover { position: absolute; left: 624px; top: 0; width: 576px; height: 864px; overflow: hidden; }

  .front-photo {
    position: absolute; inset: 0;
    background:
      /* patterned top, lower right */
      radial-gradient(ellipse 26% 22% at 92% 80%, var(--top-red) 0%, transparent 70%),
      radial-gradient(ellipse 40% 34% at 96% 88%, var(--top-navy) 0%, #2d3a4a 45%, transparent 75%),
      /* skin tone, centre */
      radial-gradient(ellipse 28% 34% at 58% 40%, var(--skin-light) 0%, #e8b88a 45%, transparent 100%),
      radial-gradient(ellipse 20% 22% at 48% 66%, #d9a07a 0%, transparent 100%),
      /* hair framing */
      radial-gradient(ellipse 46% 56% at 55% 42%, var(--skin-warm) 0%, var(--hair-gold) 55%, var(--hair-copper) 72%, transparent 86%),
      radial-gradient(ellipse 18% 45% at 22% 62%, #b88352 0%, transparent 100%),
      radial-gradient(ellipse 16% 40% at 88% 48%, #9c6a3c 0%, transparent 100%),
      /* landscape */
      radial-gradient(ellipse 40% 30% at 8% 12%, #8fb0a6 0%, transparent 100%),
      radial-gradient(ellipse 30% 40% at 100% 10%, #56703f 0%, transparent 100%),
      linear-gradient(180deg, var(--land-teal) 0%, var(--land-green) 40%, #7a6a3e 75%, #4c4a30 100%);
  }
  .front-vignette {
    position: absolute; inset: 0;
    background: radial-gradient(ellipse 75% 70% at 55% 45%, transparent 60%, rgba(30, 30, 20, 0.35) 100%);
  }

  .title {
    position: absolute; text-align: center; color: var(--ink-white);
    font-family: "Cinzel", serif; font-weight: 400;
    text-shadow: 2px 3px 6px var(--shadow); line-height: 1;
  }
  .title span { display: block; }

  .back-title { left: 0; width: 616px; top: 84px; }
  .back-title .line-top { font-size: 74px; }
  .back-title .line-mid { font-size: 34px; letter-spacing: 6px; margin-top: 8px; }
  .back-title .line-big { font-size: 112px; margin-top: 2px; }

  .synopsis {
    position: absolute; left: 28px; top: 306px; width: 518px;
    color: var(--ink-white);
    font-family: "Montserrat", sans-serif; font-weight: 400;
    font-size: 16px; line-height: 22.4px; letter-spacing: 1.1px;
    text-align: justify; text-indent: 26px;
    text-shadow: 1px 1px 3px rgba(0,0,0,0.35);
  }

  .spine-title {
    position: absolute; left: 9px; top: 90px; writing-mode: vertical-rl;
    font-family: "Cinzel", serif; font-size: 27px; color: var(--ink-white); white-space: nowrap;
  }
  .spine-author {
    position: absolute; left: 15px; top: 604px; writing-mode: vertical-rl;
    font-family: "Montserrat", sans-serif; font-weight: 500;
    font-size: 12px; letter-spacing: 7px; color: var(--ink-white); white-space: nowrap;
  }

  .front-title { left: 12px; width: 576px; top: 548px; }
  .front-title .line-top { font-size: 82px; }
  .front-title .line-mid { font-size: 42px; letter-spacing: 8px; margin-top: 10px; }
  .front-title .line-big { font-size: 150px; margin-top: -4px; }

  .front-author {
    position: absolute; left: 0; width: 600px; top: 808px; text-align: center;
    font-family: "Montserrat", sans-serif; font-weight: 600;
    font-size: 18px; letter-spacing: 8px; color: var(--ink-white);
    text-shadow: 1px 2px 4px var(--shadow);
  }
</style>
</head>
<body>
<main class="cover-spread">
  <section class="back-cover">
    <div class="back-backdrop" role="img" aria-label="Soft-focus green hillside landscape"></div>
    <h2 class="title back-title">
      <span class="line-top">Static</span>
      <span class="line-mid">Beneath My</span>
      <span class="line-big">Skin</span>
    </h2>
    <p class="synopsis">Static Beneath My Skin is an acutely honest and often highly entertaining memoir by Dorothea Quell about life with Asperger's Syndrome. The book follows Dorothea in exploring her past and takes the reader with her on her journey to receiving and accepting her diagnosis. Instead of rehashing widely available Asperger's information, Dorothea focuses on discussing the thoughts, feelings and ideas that go along with being an Aspie, giving us a rare peek into what it really feels like to be a person on the spectrum. A must read for all those who enjoy deep personal stories or have a loved one on the spectrum that they wish to understand better.</p>
  </section>

  <section class="spine">
    <span class="spine-title">Static Beneath My Skin</span>
    <span class="spine-author">DOROTHEA QUELL</span>
  </section>

  <section class="front-cover">
    <div class="front-photo" role="img" aria-label="Warm-toned close-up photo of the author with long golden hair, looking upward and smiling, wearing a dark floral top, against a blurred green landscape"></div>
    <div class="front-vignette"></div>
    <h1 class="title front-title">
      <span class="line-top">Static</span>
      <span class="line-mid">Beneath My</span>
      <span class="line-big">Skin</span>
    </h1>
    <p class="front-author">DOROTHEA QUELL</p>
  </section>
</main>
</body>
</html>
```